Marrowgate Auctions Business Cards Design Needed

I need a business card design that is modern looking - double sided (maybe just my logo on the back, but open to suggestions) - the overall design is up to you. I want it to be easy to read - not over the top flashy. I already have a company logo which I uploaded so that needs to be used. The colors of my logo are the colors I want on the card... so blue and gray (do need to match the logo colors).

Requirements
Must have
• Would like the card to be sleek, modern and easy to ready

```html
<!DOCTYPE html>
<html lang="en">
<head>
<meta charset="utf-8">
<title>Marrowgate Auctions – Business Cards</title>
<link href="https://fonts.googleapis.com/css2?family=Oswald:wght@500;600&family=Open+Sans:wght@400;600&display=swap" rel="stylesheet">
<style>
  :root {
    --page: #e9e6e2;
    --card: #1f1f20;
    --card-deep: #181819;
    --blue: #2a78bd;
    --gray: #55575a;
    --white: #f2f2f2;
  }
  html, body {
    margin: 0;
    width: 1200px;
    height: 1200px;
    overflow: hidden;
    background: var(--page);
  }
  .sheet {
    width: 1200px;
    height: 1200px;
    display: flex;
    flex-direction: column;
    align-items: center;
    justify-content: center;
    gap: 60px;
  }
  .card {
    position: relative;
    width: 900px;
    height: 514px;
    background: var(--card);
    box-shadow: 0 10px 28px rgba(0,0,0,.25);
    overflow: hidden;
  }

  /* Back side */
  .back-block {
    position: absolute;
    left: 40px;
    top: 60px;
    width: 390px;
    height: 390px;
    background: var(--card-deep);
  }
  .back-brand {
    position: absolute;
    right: 70px;
    top: 50%;
    transform: translateY(-50%);
    display: flex;
    align-items: center;
    gap: 14px;
    font-family: "Oswald", sans-serif;
    font-weight: 600;
    font-size: 38px;
    letter-spacing: 2px;
    text-transform: uppercase;
    color: var(--blue);
  }
  .brand-square {
    width: 22px;
    height: 22px;
    background: var(--blue);
    flex: none;
  }

  /* Front side */
  .front-brand {
    position: absolute;
    left: 60px;
    top: 90px;
    display: flex;
    align-items: center;
    gap: 18px;
    font-family: "Oswald", sans-serif;
    font-weight: 600;
    font-size: 62px;
    line-height: 1.05;
    letter-spacing: 3px;
    text-transform: uppercase;
    color: var(--gray);
  }
  .front-brand .brand-square {
    width: 34px;
    height: 34px;
  }
  .contact-block {
    position: absolute;
    left: 470px;
    top: 260px;
  }
  .person {
    border-left: 5px solid var(--blue);
    padding-left: 16px;
    margin-bottom: 26px;
  }
  .person-name {
    margin: 0;
    font-family: "Oswald", sans-serif;
    font-weight: 500;
    font-size: 42px;
    line-height: 1;
    color: var(--blue);
    text-transform: uppercase;
  }
  .person-title {
    margin: 6px 0 0;
    font-family: "Open Sans", sans-serif;
    font-size: 17px;
    color: var(--white);
    text-transform: uppercase;
  }
  .contacts {
    list-style: none;
    margin: 0;
    padding: 0 0 0 16px;
    border-left: 5px solid var(--blue);
    font-family: "Open Sans", sans-serif;
    font-size: 19px;
    color: var(--white);
  }
  .contacts li {
    display: flex;
    align-items: center;
    gap: 12px;
    line-height: 1.6;
  }
  .contacts svg {
    width: 16px;
    height: 16px;
    flex: none;
  }
</style>
</head>
<body>
<main class="sheet">

  <section class="card card-back" aria-label="Card back">
    <div class="back-block"></div>
    <div class="back-brand"><span class="brand-square"></span>Marrowgate Auctions</div>
  </section>

  <section class="card card-front" aria-label="Card front">
    <div class="front-brand"><span class="brand-square"></span><span>Marrowgate<br>Auctions</span></div>

    <div class="contact-block">
      <div class="person">
        <h1 class="person-name">Owen Castell</h1>
        <p class="person-title">Owner / President</p>
      </div>
      <ul class="contacts">
        <li>
          <svg viewBox="0 0 16 16" aria-hidden="true"><path fill="#2a78bd" d="M3.6 1.5l2.3 2.6-1.2 1.6c.9 1.9 2.2 3.2 4.1 4.1l1.6-1.2 2.6 2.3-1.3 2.3C6.5 13 3 9.5 1.3 4.5z"/></svg>
          +702-555-0187
        </li>
        <li>
          <svg viewBox="0 0 16 16" aria-hidden="true"><rect x="1" y="3" width="14" height="10" fill="#2a78bd"/><path d="M1 3l7 6 7-6" fill="none" stroke="#1f1f20" stroke-width="1.4"/></svg>
          hello@marrowgateauctions.com
        </li>
        <li>
          <svg viewBox="0 0 16 16" aria-hidden="true"><circle cx="8" cy="8" r="6.5" fill="none" stroke="#2a78bd" stroke-width="1.5"/><path d="M1.5 8h13M8 1.5c-3 3.5-3 9.5 0 13M8 1.5c3 3.5 3 9.5 0 13" fill="none" stroke="#2a78bd" stroke-width="1.2"/></svg>
          www.lotrescuehouse.com
        </li>
      </ul>
    </div>
  </section>

</main>
</body>
</html>
```